Book cover for a very impressive real-life healing story from a stage IV deadly disease

I need a book cover design for the French translation of the US book http://www.pagevendo.com/Tims-Journey-Fever-Outlasted-Illness/dp/0845512097/ref=sr_1_4?s=books&ie=UTF8&qid=1455100794&sr=1-4&keywords=kit+marsh
.
I do not want the word AIDS on the French cover, as the story of this book applies to any disease.

The french title will be something like :
Un nouveau matin !
Condamné par la médecine, il guérit grâce au jeûne, la détoxination, et l’amour.

which means something like
A new morning!
Subtitle : Given up by official medecine, he managed to heal with fasting, detox and love.

Many thanks !

Target Market(s)

Anybody interested in natural health

Requirements
Must have
• Nothing special
Nice to have
• Nothing special
Should not have
• Nothing special

```html
<!DOCTYPE html>
<html lang="fr">
<head>
<meta charset="utf-8">
<title>Un nouveau matin ! — couverture</title>
<link href="https://fonts.googleapis.com/css2?family=Questrial&family=Roboto+Condensed:wght@500&display=swap" rel="stylesheet">
<style>
  :root {
    --ink: #000000;
    --sky-top: #c9a83e;
    --sky-glow: #f3bd3c;
    --sky-sun: #f39a28;
    --sky-low: #d8622a;
    --city: #6b2a1c;
    --rule: #8a8a8a;
    --subtitle: #e6e6e6;
    --silver-light: #ffffff;
    --silver-mid: #c9c9c9;
    --silver-dark: #6f6f6f;
  }
  html, body {
    margin: 0;
    padding: 0;
    overflow: hidden;
    background: var(--ink);
  }
  .cover {
    position: relative;
    width: 927px;
    height: 1200px;
    overflow: hidden;
    background: var(--ink);
  }
  .cover-photo {
    position: absolute;
    left: 0;
    top: 0;
    width: 927px;
    height: 840px;
    background:
      radial-gradient(ellipse 420px 300px at 560px 430px, rgba(255, 214, 90, 0.55), rgba(255, 214, 90, 0) 70%),
      linear-gradient(180deg,
        var(--sky-top) 0%,
        var(--sky-glow) 30%,
        var(--sky-sun) 50%,
        var(--sky-low) 62%,
        var(--city) 74%,
        #2a0f0a 86%,
        var(--ink) 100%);
  }
  .cover-hill {
    position: absolute;
    left: 0;
    top: 670px;
    width: 927px;
    height: 170px;
  }
  .subtitle {
    position: absolute;
    left: 96px;
    width: 750px;
    top: 763px;
    height: 42px;
    margin: 0;
    border-top: 1px solid var(--rule);
    border-bottom: 1px solid var(--rule);
    display: flex;
    align-items: center;
    justify-content: center;
    font-family: "Roboto Condensed", "Arial Narrow", sans-serif;
    font-weight: 500;
    font-size: 19px;
    color: var(--subtitle);
    white-space: nowrap;
  }
  .title {
    position: absolute;
    left: 0;
    top: 812px;
    width: 927px;
    margin: 0;
    text-align: center;
    font-family: "Questrial", "Helvetica Neue", sans-serif;
    font-weight: 400;
    text-transform: uppercase;
    line-height: 1;
    background: linear-gradient(180deg, var(--silver-light) 0%, var(--silver-mid) 45%, var(--silver-dark) 100%);
    -webkit-background-clip: text;
    background-clip: text;
    color: transparent;
  }
  .title-line {
    display: block;
  }
  .title-line--first {
    font-size: 126px;
    letter-spacing: 2px;
    height: 160px;
    line-height: 160px;
  }
  .title-line--second {
    font-size: 150px;
    letter-spacing: 3px;
    height: 150px;
    line-height: 150px;
  }
  .byline {
    position: absolute;
    left: 96px;
    width: 750px;
    top: 1128px;
    height: 42px;
    margin: 0;
    border-top: 1px solid var(--rule);
    border-bottom: 1px solid var(--rule);
    display: flex;
    align-items: center;
    justify-content: center;
    font-family: "Questrial", "Helvetica Neue", sans-serif;
    font-size: 30px;
    letter-spacing: 1px;
    color: var(--silver-mid);
  }
</style>
</head>
<body>
  <main class="cover">
    <div class="cover-photo" role="img" aria-label="Photograph of a woman in a dark top and red skirt leaping with arms spread above a hazy city at sunset, birds flying in a golden orange sky"></div>
    <svg class="cover-hill" viewBox="0 0 927 170" aria-hidden="true">
      <path d="M0 95 L480 95 C560 40 640 18 720 14 C800 12 870 22 927 30 L927 170 L0 170 Z" fill="#000000"/>
    </svg>
    <p class="subtitle">Condamné par la médecine, il guérit grâce au jeûne, la détoxination, et l’amour</p>
    <h1 class="title">
      <span class="title-line title-line--first">Un nouveau</span>
      <span class="title-line title-line--second">matin !</span>
    </h1>
    <p class="byline">BY TIM</p>
  </main>
</body>
</html>
```